New IT Consulting Company needs new Branding

I need some business cards and logo created for new IT consulting company called Cobaltwave Partners Pty Ltd.

We deal with enterprise IT solution and IT consulting Firm.
Assisting businesses with Technology Upgrades and System integration

We have no existing color schemes in mind but after something a little recognizable but elegant also.

We are looking for something that conveys a professional look.

Target Market(s)

Targeting small to medium businesses with 0-500 employees

Industry/Entity Type

Information Technology

Contact Information for Business Card

Name, Title , Mobile Contact, Phone Contact , Email and Website URL

Logo Text

Cobaltwave Pty Ltd "Building IT Solutions the right way"

Font styles to use
Serif
Sans Serif

Requirements
Nice to have
• Looking for one or two primary colors and sticking to geometric or symmetrical design for the logo

```html
<!DOCTYPE html>
<html lang="en">
<head>
<meta charset="utf-8">
<title>Cobaltwave Partners Pty Ltd – Business Cards</title>
<link rel="stylesheet" href="https://fonts.googleapis.com/css2?family=Lato:wght@400;700&display=swap">
<style>
  :root {
    --cobalt: #1592d3;
    --cobalt-deep: #0f84c4;
    --cobalt-faint: rgba(255,255,255,0.16);
    --paper: #ffffff;
    --paper-shade: #f1f2f3;
    --rule: #4a4c4f;
    --backdrop: #e7e9ec;
    --ink-light: #ffffff;
  }
  * { box-sizing: border-box; margin: 0; padding: 0; }
  html, body { width: 1200px; height: 900px; overflow: hidden; }
  body {
    background: var(--backdrop);
    font-family: "Lato", Arial, sans-serif;
    display: flex;
    align-items: center;
    justify-content: center;
    gap: 40px;
  }
  .card {
    position: relative;
    width: 540px;
    height: 309px;
    overflow: hidden;
    box-shadow: 0 6px 18px rgba(0,0,0,0.15);
  }

  /* Front */
  .card-front {
    background: var(--cobalt);
    display: flex;
    align-items: center;
    justify-content: center;
  }
  .front-ring {
    position: absolute;
    left: 50%; top: 50%;
    width: 270px; height: 270px;
    transform: translate(-50%, -50%);
    border-radius: 50%;
    border: 6px solid var(--cobalt-faint);
    background: rgba(0,0,0,0.04);
  }
  .front-name {
    position: relative;
    color: var(--ink-light);
    font-weight: 700;
    text-transform: uppercase;
    text-align: center;
    line-height: 1.05;
  }
  .front-name .line-main { display: block; font-size: 44px; letter-spacing: 1px; }
  .front-name .line-sub { display: block; font-size: 22px; letter-spacing: 6px; }

  /* Back */
  .card-back {
    background: linear-gradient(var(--paper), var(--paper-shade) 165px, var(--paper) 165px);
  }
  .back-rule {
    position: absolute;
    left: 0; right: 0; top: 165px;
    height: 4px;
    background: var(--rule);
  }
  .back-band {
    position: absolute;
    left: 0; right: 0; top: 176px; bottom: 0;
    background: var(--cobalt);
  }
  .brand {
    position: absolute;
    left: 48px; top: 46px;
    display: flex;
    align-items: center;
    gap: 20px;
  }
  .brand-dot {
    width: 72px; height: 72px;
    border-radius: 50%;
    background: var(--cobalt);
    border: 5px solid var(--rule);
  }
  .brand-name {
    color: var(--cobalt);
    font-weight: 700;
    text-transform: uppercase;
    line-height: 1.1;
  }
  .brand-name .line-main { display: block; font-size: 31px; letter-spacing: 0.5px; }
  .brand-name .line-sub { display: block; font-size: 17px; letter-spacing: 4px; }

  .person {
    position: absolute;
    left: 40px; top: 190px;
    width: 220px;
    text-align: right;
    color: var(--ink-light);
  }
  .person-name { font-size: 21px; font-weight: 700; }
  .person-title { font-size: 13px; margin-top: 2px; }
  .person-address { font-size: 14px; margin-top: 10px; line-height: 1.4; }

  .contacts {
    position: absolute;
    left: 290px; top: 192px;
    list-style: none;
    color: var(--ink-light);
    font-size: 13.5px;
  }
  .contacts li {
    display: flex;
    align-items: center;
    gap: 8px;
    height: 22px;
  }
  .contact-icon {
    width: 15px; height: 15px;
    background: var(--ink-light);
    border-radius: 2px;
    display: flex; align-items: center; justify-content: center;
  }
  .contact-icon svg { width: 11px; height: 11px; fill: var(--cobalt-deep); stroke: var(--cobalt-deep); }
</style>
</head>
<body>

  <section class="card card-front" aria-label="Business card front">
    <div class="front-ring"></div>
    <h1 class="front-name">
      <span class="line-main">Cobaltwave</span>
      <span class="line-sub">Partners Pty Ltd</span>
    </h1>
  </section>

  <section class="card card-back" aria-label="Business card back">
    <div class="brand">
      <div class="brand-dot"></div>
      <h2 class="brand-name">
        <span class="line-main">Cobaltwave</span>
        <span class="line-sub">Partners Pty Ltd</span>
      </h2>
    </div>
    <div class="back-rule"></div>
    <div class="back-band"></div>

    <div class="person">
      <p class="person-name">Daniel Reeves</p>
      <p class="person-title">Managing Director</p>
      <p class="person-address">1234, Address GoesHere<br>Country, 12345</p>
    </div>

    <ul class="contacts">
      <li>
        <span class="contact-icon"><svg viewBox="0 0 12 12"><path stroke="none" d="M1 4c0-2 1-3 5-3s5 1 5 3l-2 1-1-1.5H4L3 5z M3 6h6l1 5H2z"/></svg></span>
        123-456-7890
      </li>
      <li>
        <span class="contact-icon"><svg viewBox="0 0 12 12"><rect stroke="none" x="3" y="0.5" width="6" height="11" rx="1"/></svg></span>
        123-456-7890
      </li>
      <li>
        <span class="contact-icon"><svg viewBox="0 0 12 12"><rect x="1" y="2.5" width="10" height="7" fill="none" stroke-width="1.4"/><path d="M1 2.5l5 4 5-4" fill="none" stroke-width="1.4"/></svg></span>
        info@youremail.com
      </li>
      <li>
        <span class="contact-icon"><svg viewBox="0 0 12 12"><path d="M5 7l2-2 M4 5L2.5 6.5a2 2 0 0 0 3 3L7 8 M8 7l1.5-1.5a2 2 0 0 0-3-3L5 4" fill="none" stroke-width="1.4" stroke-linecap="round"/></svg></span>
        www.yourweb.com
      </li>
    </ul>
  </section>

</body>
</html>
```